Website incl. html for real estate project

We need the design and implementation of a website for a real estate project. Condominiums are built, which are sold.
We upload the sales brochure. The website should be based on the design of the sales brochure.
There are three houses with 5 apartments each. It should be rendered like this. The structure of the menu should be roughly as follows. Most information about the content is either in the appendix as a picture or in the brochure (PDF)):
Home (page 4-5 from the brochure)
House A
house B
house c
overview
basement
Municipal elections (page 6-7 in the brochure pdf)
Contact
Please use Roboto Regular as font.
And one page should give an overview of all apartments with the prices, the living space, etc. as on the file overview2.jpg.
If you go to the House A, House B, or House C menus, a page should come up with the details for that house only. The pages in the brochure are:
House A (Page 10-11)
House B (page 22-23)
House C (page 34-35)
The individual apartments should each be shown on a property page. There the plan / floor plan of the apartment and the pictures from the inside should be shown. As with the object page.jpg attachment.
Für die Designer... Mehr Zeit...
Coded - Design and coding required
1 page

```html
<!DOCTYPE html>
<html lang="de">
<head>
<meta charset="utf-8">
<title>Wohnpark am Ahorn</title>
<link href="https://fonts.googleapis.com/css2?family=Roboto:wght@400;500;700&display=swap" rel="stylesheet">
<style>
:root{
  --ink:#1D2831;
  --blue:#008DD1;
  --paper:#f9f9fb;
  --white:#ffffff;
  --text:#6b7178;
  --line:#e3e6ea;
}
*{box-sizing:border-box;margin:0;padding:0}
html,body{width:1200px;height:3309px;overflow:hidden;background:var(--paper);font-family:'Roboto',sans-serif;color:var(--ink)}
.page{position:relative;width:1200px;height:3309px;background:var(--white)}
.abs{position:absolute}

/* nav */
.nav{left:0;top:0;width:1200px;height:77px;display:flex;align-items:center;padding:0 16px}
.brand{display:flex;align-items:center;gap:8px;width:199px}
.brand-mark{width:10px;height:10px;background:var(--blue)}
.brand-name{font-weight:500;font-size:15px;color:var(--ink)}
.menu{display:flex;gap:4px;list-style:none}
.menu li{font-size:8.5px;letter-spacing:.4px;color:var(--text);padding:7px 10px;text-transform:uppercase}
.menu li.active{background:#eef0f2;color:var(--ink)}
.nav-contact{margin-left:auto;font-size:8.5px;color:var(--text)}

/* hero */
.hero{left:16px;top:77px;width:1168px;height:662px;background:linear-gradient(180deg,#9ccbe9 0%,#cfe4f0 38%,#b9c2bf 55%,#7fa35a 68%,#4f7d2c 100%)}
.hotspot{position:absolute;width:18px;height:18px;border-radius:50%;background:var(--blue);border:3px solid rgba(255,255,255,.7)}

/* band */
.band{left:0;top:739px;width:1200px;height:273px;background:var(--blue);text-align:center;color:var(--white)}
.band h1{font-size:48px;font-weight:500;margin-top:70px}
.band p{font-size:11px;margin-top:18px}

/* price table */
.labels{left:16px;top:948px;width:140px;height:237px;background:var(--white);padding:48px 14px 0}
.labels div{font-size:8.5px;color:var(--text);border-bottom:1px solid var(--line);height:28px;padding-top:4px}
.labels div.tall{height:49px}
.house{top:948px;width:330px;height:237px;background:var(--white);padding:0 16px}
.house h3{text-align:center;font-size:18px;font-weight:700;padding:16px 0 10px}
.house h3 span{color:var(--blue);text-decoration:underline}
.row{display:grid;grid-template-columns:80px 60px 1fr 60px;font-size:8.5px;color:var(--text);border-bottom:1px solid var(--line);height:28px;padding-top:4px;line-height:1.2}
.row.tall{height:49px}
.row span:last-child{text-align:right}

/* intro */
.section-title{width:1200px;text-align:center;font-size:24px;font-weight:400}
.section-title::before{content:"";display:block;width:28px;height:2px;background:var(--ink);margin:0 auto 18px}
.copy{font-size:10px;line-height:19px;color:var(--text)}
.photo{top:1584px;height:197px}

/* stats */
.stat{top:2073px;width:134px;height:141px;text-align:center;padding-top:22px}
.stat b{display:block;font-size:40px;font-weight:700;line-height:48px}
.stat small{display:block;font-size:9px;line-height:14px;margin:8px auto 0;width:90px}
.stat.outline{border:2px solid var(--blue);color:#6f7378;background:var(--white)}
.stat.outline small{color:var(--text)}
.stat.blue{background:var(--blue);color:var(--white)}
.stat.dark{background:var(--ink);color:var(--white)}

/* contact */
.contact{left:0;top:2288px;width:1200px;height:592px;background:var(--paper)}
.map{left:242px;top:2480px;width:320px;height:320px;border-radius:50%;background:radial-gradient(circle,#f1f1f1 0%,#e6e6e8 100%)}
.form-title{left:618px;top:2480px;font-size:26px;font-weight:500}
.form-lead{left:618px;top:2527px;width:340px;font-size:10px;line-height:17px;color:var(--text)}
.field{background:var(--white);border:1px solid #dcdfe3;font-size:8.5px;color:#9aa0a6;padding:8px 9px}
.btn{left:618px;top:2769px;width:100px;height:35px;background:var(--blue);color:var(--white);font-size:8.5px;font-weight:700;display:flex;align-items:center;justify-content:center}

/* footer */
.foot-col{top:2950px}
.foot-col h4{font-size:13px;font-weight:500;margin-bottom:22px}
.foot-col p,.foot-col li{font-size:9px;line-height:20px;color:var(--text);list-style:none}
.foot-col li{text-transform:uppercase;letter-spacing:.3px}
.social{display:flex;flex-direction:column;gap:9px}
.social i{width:9px;height:9px;border-radius:50%;background:var(--ink);display:block}
.news{display:flex;width:246px;height:34px;border:1px solid #cfd3d8;margin-top:-2px}
.news span{flex:1;font-size:8px;color:#9aa0a6;padding:11px 9px}
.news b{width:36px;background:var(--ink);display:flex;align-items:center;justify-content:center}
.rule{left:16px;top:3191px;width:1168px;height:1px;background:var(--line)}
.copyright{left:16px;top:3212px;font-size:8px;color:var(--text)}
</style>
</head>
<body>
<div class="page">

  <header class="nav abs">
    <div class="brand"><span class="brand-mark"></span><span class="brand-name">Arvena Immobilien</span></div>
    <ul class="menu">
      <li class="active">Startseite</li><li>Haus A</li><li>Haus B</li><li>Haus C</li><li>Untergeschoss</li><li>Gemeinde Birkwil</li><li>Kontakt</li>
    </ul>
    <div class="nav-contact">Tel +41 00 700 12 34 &nbsp;|&nbsp; info@arvena-immo.example</div>
  </header>

  <div class="hero abs" role="img" aria-label="Aussenansicht der drei Wohnhäuser mit Wiese und Bäumen">
    <span class="hotspot" style="left:207px;top:232px"></span>
    <span class="hotspot" style="left:611px;top:309px"></span>
    <span class="hotspot" style="left:1013px;top:284px"></span>
  </div>

  <section class="band abs">
    <h1>Wohnpark am Ahorn</h1>
    <p>Hochwertige und moderne Eigentumswohnungen an der Birkenstrasse/Feldweg in Birkwil</p>
  </section>

  <div class="labels abs">
    <div>Attika</div><div>Obergeschoss</div><div>Obergeschoss</div><div class="tall">Erdgeschoss</div><div class="tall">Erdgeschoss</div>
  </div>

  <div class="house abs" style="left:169px">
    <h3>Haus <span>A</span></h3>
    <div class="row"><span>4.5 Zimmer</span><span>108 m2</span><span>105 m2<br>Sonnenterrasse</span><span>945,000 CHF</span></div>
    <div class="row"><span>3.5 Zimmer</span><span>81 m2</span><span>16 m2 Balkon</span><span>754,000 CHF</span></div>
    <div class="row"><span>4.5 Zimmer</span><span>102 m2</span><span>33 m2 Balkon</span><span>640,000 CHF</span></div>
    <div class="row tall"><span>3.5 Zimmer</span><span>81 m2</span><span>16 m2 gedeckter<br>Sitzplatz &amp;<br>eigener Garten</span><span>657,000 CHF</span></div>
    <div class="row tall"><span>4.5 Zimmer</span><span>102 m2</span><span>33 m2 gedeckter<br>Sitzplatz &amp;<br>eigener Garten</span><span>765,000 CHF</span></div>
  </div>
  <div class="house abs" style="left:511px">
    <h3>Haus <span>B</span></h3>
    <div class="row"><span>4.5 Zimmer</span><span>108 m2</span><span>105 m2<br>Sonnenterrasse</span><span>945,000 CHF</span></div>
    <div class="row"><span>3.5 Zimmer</span><span>81 m2</span><span>16 m2 Balkon</span><span>754,000 CHF</span></div>
    <div class="row"><span>4.5 Zimmer</span><span>102 m2</span><span>33 m2 Balkon</span><span>640,000 CHF</span></div>
    <div class="row tall"><span>3.5 Zimmer</span><span>81 m2</span><span>16 m2 gedeckter<br>Sitzplatz &amp;<br>eigener Garten</span><span>657,000 CHF</span></div>
    <div class="row tall"><span>4.5 Zimmer</span><span>102 m2</span><span>33 m2 gedeckter<br>Sitzplatz &amp;<br>eigener Garten</span><span>765,000 CHF</span></div>
  </div>
  <div class="house abs" style="left:853px">
    <h3>Haus <span>C</span></h3>
    <div class="row"><span>4.5 Zimmer</span><span>108 m2</span><span>105 m2<br>Sonnenterrasse</span><span>945,000 CHF</span></div>
    <div class="row"><span>3.5 Zimmer</span><span>81 m2</span><span>16 m2 Balkon</span><span>754,000 CHF</span></div>
    <div class="row"><span>4.5 Zimmer</span><span>102 m2</span><span>33 m2 Balkon</span><span>640,000 CHF</span></div>
    <div class="row tall"><span>3.5 Zimmer</span><span>81 m2</span><span>16 m2 gedeckter<br>Sitzplatz &amp;<br>eigener Garten</span><span>657,000 CHF</span></div>
    <div class="row tall"><span>4.5 Zimmer</span><span>102 m2</span><span>33 m2 gedeckter<br>Sitzplatz &amp;<br>eigener Garten</span><span>765,000 CHF</span></div>
  </div>

  <h2 class="section-title abs" style="left:0;top:1296px">Wohnpark am Ahorn</h2>

  <p class="copy abs" style="left:244px;top:1390px;width:316px">Die Überbauung mit drei Mehrfamilienhäusern und insgesamt 15 Eigentumswohnungen entsteht zwischen der Birkenstrasse und dem Feldweg in Birkwil bei Talmatt.</p>
  <p class="copy abs" style="left:630px;top:1390px;width:316px">Das Gebäude wird mit 18 bis 30 cm atmungsaktiver Steinwolle isoliert. Geheizt wird über eine moderne Wärmepumpe im Verbund mit einer Photovoltaikanlage, ökologisch hocheffizient mit zeitgemässer Technologie, unabhängig von steigenden Gas und Ölpreisen.</p>
  <p class="copy abs" style="left:244px;top:1491px;width:316px">Die modernen und hochwertigen Wohnungen sind gegen das ruhige Quartier Sonnmatt und den wunderschönen Ausblick auf den grünen «Lindenhügel» ausgerichtet.</p>
  <p class="copy abs" style="left:630px;top:1491px;width:316px">Alle Wohnungen besitzen einen grosszügigen Wohn-, Koch-/ Essbereich mit raumhohen Fenstern verglast, was für eine helle und freundliche Atmosphäre sorgt.</p>

  <div class="photo abs" style="left:244px;width:151px;background:linear-gradient(160deg,#e9e6e1,#bdb4a8)" role="img" aria-label="Badezimmer mit Waschtisch und Spiegel"></div>
  <div class="photo abs" style="left:408px;width:385px;background:linear-gradient(170deg,#f2f1ef,#c9c5bf 70%,#8f8a84)" role="img" aria-label="Offener Wohn- und Essbereich mit Küche"></div>
  <div class="photo abs" style="left:805px;width:151px;background:linear-gradient(160deg,#eef0f2,#c8c2b9)" role="img" aria-label="Helles Schlafzimmer mit Fenster"></div>

  <p class="copy abs" style="left:244px;top:1820px;width:316px">Die Wohnungen befinden sich an idealer Lage in Birkwil mit guter Besonnung und die nächste Bushaltestelle ist nur knapp 120 Meter entfernt. Die Wohnungen sind im Obergeschoss mit grosszügigem Balkon und im Erdgeschoss mit einem gedeckten Sitzplatz und eigenem Garten ausgestattet.</p>
  <p class="copy abs" style="left:652px;top:1820px;width:316px">Die Umgebungsgestaltung passt perfekt in die ruhige, natürliche und trotzdem moderne Umgebung. Die grosszügigen Grünflächen der Erdgeschosswohnungen und die dezente Grundbepflanzung verbunden mit den Wegen runden die moderne und zeitlose Architektur des Gebäudes ab.</p>
  <p class="copy abs" style="left:244px;top:1940px;width:316px">Der Wohnpark verfügt über ein grosszügiges, gemeinsames Parkhaus, von dem aus in jedes Gebäude ein Lift auf die gewünschte Etage führt. Jede Wohnung verfügt über einen eigenen Keller / ein eigenes Kellerabteil. Zudem ist im Keller ein Schutzraum für die Bewohner vorhanden.</p>
  <p class="copy abs" style="left:650px;top:1940px;width:316px">Die Wohnungen werden schlüsselfertig zum Fixpreis abgegeben. Es besteht darüber hinaus die Möglichkeit den Innenausbau nach eigenen Wünschen in verschiedenen Bereichen massgeblich mitzugestalten.</p>

  <div class="stat outline abs" style="left:244px"><b>3</b><small>Gebäude mit individuellem Wohnangebot</small></div>
  <div class="stat blue abs" style="left:390px"><b>9</b><small>unterschiedliche Grundrisstypen</small></div>
  <div class="stat dark abs" style="left:535px"><b>27</b><small>Parkplätze in der Tiefgarage</small></div>
  <div class="stat blue abs" style="left:680px"><b>15</b><small>komfortable Wohnungen</small></div>
  <div class="stat outline abs" style="left:824px"><b>12</b><small>Meter bis zur Bushaltestelle</small></div>

  <section class="contact abs"></section>
  <h2 class="section-title abs" style="left:0;top:2364px">Kontakt</h2>
  <div class="map abs" role="img" aria-label="Lagekarte des Wohnparks in Birkwil"></div>
  <h3 class="form-title abs">Schreiben Sie Uns</h3>
  <p class="form-lead abs">Lorem ipsum proin gravida nibh vel velit auctor aliollicitudin, lorem quis bibendum auctor nisi elit consequat ipsum, nec sagittis.</p>
  <div class="field abs" style="left:618px;top:2588px;width:162px;height:28px">Name</div>
  <div class="field abs" style="left:794px;top:2588px;width:162px;height:28px">Email</div>
  <div class="field abs" style="left:618px;top:2627px;width:338px;height:131px">Comment</div>
  <div class="btn abs">GET IN TOUCH &raquo;</div>

  <div class="foot-col abs" style="left:16px;top:2978px">
    <div class="brand" style="margin-bottom:16px"><span class="brand-mark"></span><span class="brand-name">Arvena Immobilien</span></div>
    <p>Arvena Immobilien AG<br>Ahornweg 12<br>9990 Birkwil</p>
  </div>
  <div class="foot-col abs" style="left:323px">
    <h4>Sitemap</h4>
    <ul><li>Startseite</li><li>Kontakt</li><li>Haus A</li><li>Haus B</li><li>Haus C</li><li>Untergeschoss</li><li>Gemeinde Birkwil</li><li>Impressum</li><li>Datenschutz</li></ul>
  </div>
  <div class="foot-col abs" style="left:630px">
    <h4>Social Media</h4>
    <div class="social"><i></i><i></i></div>
  </div>
  <div class="foot-col abs" style="left:938px">
    <h4>Newsletter</h4>
    <div class="news"><span>Your Email Address</span><b><svg width="11" height="11" viewBox="0 0 12 12"><path d="M1 6 L11 1 L8 11 L6 7 Z" fill="#fff"/></svg></b></div>
    <p style="margin-top:16px;width:246px;line-height:16px">Lorem ipsum proin gravida nibh vel velit auctor aliollicitudin, lorem quis bibendu</p>
  </div>
  <div class="rule abs"></div>
  <div class="copyright abs">© 2022 Arvena Immobilien AG – All Rights Reserved</div>

</div>
</body>
</html>
```